Forge Night Club Flyer, need asap for party this weekend

Text is drawn as an attachment

Need a flyer for club night this Saturday. Guaranteed project need quick turnaround. Image attached, and the FORGE logo to be large and detailed like a sign. The dj names KESTREL, MR. HALVORNE, AND DESMOND K. ORLEY can be large too. It's for house/electronic music in a nice classy venue. High Res image attached.

Target Market(s)

21-40 year old house music lovers, club business

Industry/Entity Type

Night Club

Font styles to use
Sans Serif

Colors
ffffff
cadf82
33a6d7
0356a4
fbee3d

Requirements
Must have
• Either the girl in hard hat or tool belt image, or something similar to stick with the Forge theme. Also the dj names needs to be the same size
Nice to have
• Faded image or some lining around the images so it doesn't look like a plain photo. Black and white is good or faded.
Should not have
• Any cursive or anything not professional looking

```html
<!DOCTYPE html>
<html lang="en">
<head>
<meta charset="utf-8">
<title>Forge – Club Night Flyer</title>
<link rel="stylesheet" href="https://fonts.googleapis.com/css2?family=Oswald:wght@500;600&family=Open+Sans:wght@700&display=swap">
<style>
  :root {
    --yellow: #fbee3d;
    --gold: #f2d600;
    --white: #ffffff;
    --blue: #0356a4;
    --blue-light: #33a6d7;
    --ink: #050608;
    --skin: #c99a7a;
    --belt: #e2a62c;
    --denim: #3f5f86;
  }
  * { margin: 0; padding: 0; box-sizing: border-box; }
  html, body { width: 1200px; height: 900px; overflow: hidden; background: var(--ink); }

  .flyer {
    position: relative;
    width: 1200px;
    height: 900px;
    overflow: hidden;
    background: var(--ink);
    font-family: "Oswald", "Arial Narrow", sans-serif;
  }

  .flyer__backdrop {
    position: absolute;
    left: 440px; top: 0;
    width: 760px; height: 900px;
    background:
      radial-gradient(circle at 55% 48%, rgba(255,255,255,0.35) 0%, rgba(140,140,145,0.25) 22%, rgba(20,20,22,0) 55%),
      radial-gradient(circle at 95% 70%, #3a3b3e 0%, #151618 40%, transparent 60%),
      linear-gradient(135deg, #2a2b2e 0%, #6b6d71 35%, #1a1b1d 70%, #000 100%);
  }

  .flyer__photo {
    position: absolute;
    left: 0; top: 0;
    width: 515px; height: 900px;
    background:
      linear-gradient(180deg, #b8343a 0%, #d8d2cf 9%, var(--skin) 16%, var(--skin) 44%, var(--belt) 52%, #c98e22 72%, var(--denim) 80%, var(--skin) 86%, #9d7256 100%);
    -webkit-mask-image: linear-gradient(90deg, #000 82%, transparent 100%);
            mask-image: linear-gradient(90deg, #000 82%, transparent 100%);
  }

  .headline {
    position: absolute;
    left: 600px; top: 50px;
    width: 540px;
    text-align: center;
    white-space: nowrap;
    font-weight: 600;
    font-size: 190px;
    line-height: 1.05;
    letter-spacing: 0;
    color: var(--gold);
  }

  .lineup-band {
    position: absolute;
    left: 480px; top: 289px;
    width: 720px; height: 275px;
    background: linear-gradient(90deg, rgba(3,86,164,0) 0%, rgba(3,86,164,0.9) 12%, var(--blue) 50%, rgba(3,86,164,0.85) 100%);
  }
  .lineup-band::after {
    content: "";
    position: absolute;
    left: 0; right: 0; bottom: 0;
    height: 40%;
    background: linear-gradient(180deg, rgba(51,166,215,0) 0%, rgba(51,166,215,0.25) 100%);
  }

  .lineup {
    position: absolute;
    left: 600px; top: 300px;
    width: 520px;
    text-align: center;
    font-weight: 500;
    line-height: 1;
    white-space: nowrap;
    z-index: 2;
  }
  .lineup__title  { font-size: 50px; color: var(--white); margin-top: 10px; letter-spacing: 1px; }
  .lineup__artist { font-size: 48px; color: var(--white); margin-top: 18px; letter-spacing: 1px; }
  .lineup__artist--headliner { color: var(--yellow); }

  .date-box {
    position: absolute;
    left: 673px; top: 589px;
    width: 380px; height: 153px;
    background: linear-gradient(180deg, #1a1b1e 0%, #000 100%);
    border: 6px solid #b9bcc1;
    border-radius: 6px;
    box-shadow: inset 0 0 0 2px #3c3e42;
    text-align: center;
    font-weight: 500;
    line-height: 1;
    padding-top: 14px;
  }
  .date-box__day  { font-size: 50px; color: var(--yellow); }
  .date-box__date { font-size: 54px; color: var(--white); margin-top: 8px; letter-spacing: 2px; }

  .venue-band {
    position: absolute;
    left: 722px; top: 768px;
    width: 478px; height: 96px;
    background: linear-gradient(90deg, rgba(3,86,164,0.55) 0%, var(--blue) 55%, var(--blue) 100%);
  }

  .venue {
    position: absolute;
    left: 752px; top: 772px;
    font-family: "Open Sans", Arial, sans-serif;
    font-style: normal;
    font-weight: 700;
    font-size: 23px;
    line-height: 30px;
    color: var(--yellow);
  }
</style>
</head>
<body>
  <main class="flyer">
    <div class="flyer__backdrop" role="img" aria-label="Black and grey abstract burst of shards with a speaker cone and turntable motif"></div>
    <div class="flyer__photo" role="img" aria-label="Photo of a woman's midriff in a tied plaid shirt and denim shorts, wearing a leather tool belt with wrenches, pliers and a hammer"></div>

    <h1 class="headline">FORGE</h1>

    <div class="lineup-band"></div>
    <section class="lineup">
      <p class="lineup__title">HOUSE &amp; TECH WORKERS</p>
      <p class="lineup__artist lineup__artist--headliner">KESTREL</p>
      <p class="lineup__artist">DESMOND K. ORLEY</p>
      <p class="lineup__artist">MR. HALVORNE</p>
    </section>

    <div class="date-box">
      <p class="date-box__day">21 SATURDAY</p>
      <p class="date-box__date">03-12-2016</p>
    </div>

    <div class="venue-band"></div>
    <address class="venue">
      OKV LOUNGE<br>
      214 N ALDER AVE<br>
      MAPLEGROVE
    </address>
  </main>
</body>
</html>
```